Hal's Remedies Business Card Design Project

I need a business card designed for my pharmacy Hal's Remedies. I would like just the logo on one side, maybe with black background and white lettering. The other side I would also like to include my logo which is attached. Also, please include my name and the following information:
Hal Norwick Owner/Pharm D.
Business address is 7163 N Birch Rd Sioux Falls, SD 57291.
Phone number is 605-318-6027 and fax # is 605-318-6031.
my email address is hal@halsremedies.example.
My website is www.halsremedies.example.
My business hours are Monday-Friday 8am-7 pm. Saturday 8am-12 pm. Sunday Closed.
I would like the design to include my logo colors, black, white, and neon green. Silver may be added as a highlight. Thanks.
Pharmacy
See above in product description

```html
<!DOCTYPE html>
<html lang="en">
<head>
<meta charset="utf-8">
<title>Hal's Remedies – Business Card</title>
<link rel="stylesheet" href="https://fonts.googleapis.com/css2?family=Open+Sans:wght@400;600;700&display=swap">
<style>
  :root {
    --canvas: #e4e4e4;
    --card-dark: #252626;
    --card-light: #ffffff;
    --ink: #231f20;
    --ink-soft: #1a1a1a;
    --neon: #acd038;
    --neon-text: #6f9a1e;
    --white: #ffffff;
  }
  * { margin: 0; padding: 0; box-sizing: border-box; }
  html, body {
    width: 1000px; height: 1200px; overflow: hidden;
    background: var(--canvas);
    font-family: "Open Sans", Arial, sans-serif;
  }
  .canvas { position: relative; width: 1000px; height: 1200px; }

  .card { position: absolute; }
  .card--front {
    left: 168px; top: 117px; width: 655px; height: 392px;
    background: var(--card-dark);
  }
  .card--back {
    left: 150px; top: 671px; width: 686px; height: 399px;
    background: var(--card-light);
  }

  .brand {
    position: absolute; left: 0; right: 0;
    display: flex; align-items: center; justify-content: center; gap: 18px;
  }
  .brand__dot {
    width: 18px; height: 18px; border-radius: 50%; background: var(--neon);
  }
  .brand__name { font-weight: 600; letter-spacing: -1px; line-height: 1; }
  .card--front .brand { top: 296px - 117px; top: 179px; }
  .card--front .brand__name { color: var(--white); font-size: 46px; }
  .card--back .brand { top: 81px; }
  .card--back .brand__name { color: var(--ink); font-size: 40px; }

  .rule {
    position: absolute; left: 81px; width: 531px; top: 167px;
    height: 1.5px; background: var(--neon);
  }

  .holder {
    position: absolute; top: 203px; left: 0; right: 0; text-align: center;
    white-space: nowrap;
  }
  .holder__name {
    font-size: 18px; font-weight: 600; letter-spacing: 1.2px; color: var(--ink-soft);
  }
  .holder__title {
    font-size: 12px; color: var(--neon-text); letter-spacing: .5px; margin-left: 6px;
  }

  .contact {
    position: absolute; top: 264px;
    display: grid; grid-template-columns: 14px auto; column-gap: 10px;
    font-size: 12.5px; font-weight: 600; line-height: 16px; color: var(--ink-soft);
  }
  .contact--address { left: 72px; }
  .contact--phone { left: 256px; }
  .contact--web { left: 424px; }
  .contact svg { width: 12px; height: 12px; margin-top: 2px; fill: var(--neon); }

  .hours {
    position: absolute; left: 0; right: 0; top: 331px; height: 28px;
    background: var(--neon);
    display: flex; align-items: center; justify-content: center;
    font-size: 12.5px; font-weight: 600; color: var(--ink-soft); letter-spacing: .2px;
  }
</style>
</head>
<body>
<main class="canvas">

  <section class="card card--front" aria-label="Card front">
    <div class="brand">
      <span class="brand__dot"></span>
      <span class="brand__name">Hal's Remedies</span>
    </div>
  </section>

  <section class="card card--back" aria-label="Card back">
    <div class="brand">
      <span class="brand__dot"></span>
      <span class="brand__name">Hal's Remedies</span>
    </div>
    <div class="rule"></div>

    <p class="holder">
      <span class="holder__name">Hal Norwick</span><span class="holder__title">Owner/Pharm D.</span>
    </p>

    <div class="contact contact--address">
      <svg viewBox="0 0 12 12"><path d="M6 1 0 6h1.7v5h3.2V8h2.2v3h3.2V6H12z"/></svg>
      <span>7163 N Birch Rd<br>Sioux Falls, SD 57291</span>
    </div>

    <div class="contact contact--phone">
      <svg viewBox="0 0 12 12"><path d="M2.4 1 4.3 3.3 3.4 4.6c.7 1.5 2.2 3 3.9 3.9l1.3-.9L11 9.6 9.7 11C5 10.6 1.2 6.8 1 2.3z"/></svg>
      <span>605-318-6027 (P)<br>#605-318-6031 (F)</span>
    </div>

    <div class="contact contact--web">
      <svg viewBox="0 0 12 12"><path d="M6 .5a5.5 5.5 0 1 0 0 11 5.5 5.5 0 0 0 0-11zm0 1c.6.6 1.1 1.8 1.3 3.5H4.7C4.9 3.3 5.4 2.1 6 1.5zM4 5H1.6A4.5 4.5 0 0 1 4.5 1.8 9 9 0 0 0 3.7 5zm-2.4 2H3.7c.1 1.2.4 2.3.8 3.2A4.5 4.5 0 0 1 1.6 7zm3.1 0h2.6C7.1 8.7 6.6 9.9 6 10.5 5.4 9.9 4.9 8.7 4.7 7zm3.6 0h2.1a4.5 4.5 0 0 1-2.9 3.2c.4-.9.7-2 .8-3.2zm0-2A9 9 0 0 0 7.5 1.8 4.5 4.5 0 0 1 10.4 5z"/></svg>
      <span>hal@halsremedies.example</span>
      <svg viewBox="0 0 12 12"><path d="M6 .8a5.2 5.2 0 1 0 2.6 9.7l-.4-.8A4.3 4.3 0 1 1 10.3 6c0 1-.4 1.6-1 1.6-.5 0-.7-.3-.7-.8V3.4h-.9v.5a2.4 2.4 0 1 0 .3 3.5c.3.6.8.9 1.4.9 1.1 0 1.8-1 1.8-2.3A5.2 5.2 0 0 0 6 .8zm0 6.8a1.6 1.6 0 1 1 0-3.2 1.6 1.6 0 0 1 0 3.2z"/></svg>
      <span>www.halsremedies.example</span>
    </div>

    <div class="hours">Monday-Friday 8am-7 pm &nbsp;●&nbsp; Saturday 8am-12 pm &nbsp;●&nbsp; Sunday Closed</div>
  </section>

</main>
</body>
</html>
```